clean web design for a recruitment company

We need a web design for a company called 'TORAVI' recruitment. We are a new age recruitment companies that selects people by their true nature, values and what they can bring to the table as a tangible talent. We are all here possessing a certain talent, whatever that could be that the world needs. The final design should communicate professionalism and strongly embedded etiquette we believe in and a branding promise 'Seeing ones true nature'. Our companies values are integrity, giving away to the community, cherishing the sharing of our talent, time and helping one another.

Target Market(s)

Gulf Countries

Industry/Entity Type

It Company

Number of Pages Required

1 page

Font styles to use
Serif

Requirements
Must have
• Clear and readable font, user friendly structure and easy navigation menus.
Nice to have
• Extra sort of ideas on images we may use, tag lines etc. sample sites we love site:https://www.velmaroque.com/
• http://www.dorisaklund.com/
• http://www.pebblemoorhouse.com/idea-gallery/
Should not have
• all sort of colors, big combination of fonts, images with people in the office or people in suits likewise all the typical industry web sites

```html
<!DOCTYPE html>
<html lang="en">
<head>
<meta charset="utf-8">
<title>TORAVI Recruitment</title>
<link href="https://fonts.googleapis.com/css2?family=Raleway:wght@300;400;500;600;700&display=swap" rel="stylesheet">
<style>
:root{
  --ink:#111;
  --white:#fff;
  --grey-band:#efefef;
  --rule:#d8d8d8;
  --muted:#555;
  --footer:#000;
  --footer-text:#bdbdbd;
  --btn-grey:#8a8a8a;
}
*{box-sizing:border-box;margin:0;padding:0}
html,body{width:1200px;height:3388px;overflow:hidden;background:var(--white)}
body{font-family:"Raleway",sans-serif;color:var(--ink);position:relative}
.abs{position:absolute}
.btn{position:absolute;display:flex;align-items:center;justify-content:center;background:var(--ink);color:var(--white);font-size:14px;font-weight:700;letter-spacing:.5px;text-transform:uppercase}
.btn-outline{position:absolute;display:flex;align-items:center;justify-content:center;border:2px solid var(--white);color:var(--white);font-size:17px;font-weight:600;text-transform:uppercase;letter-spacing:.5px}
.center{text-align:center}
.copy{font-size:14.5px;line-height:1.55;color:#222;text-align:center}

/* header */
.site-header{top:0;left:0;width:1200px;height:246px}
.brand-mark{left:571px;top:36px;width:58px;height:90px;border:3px solid var(--ink)}
.brand-name{left:0;width:1200px;top:138px;text-align:center;font-size:44px;font-weight:500;letter-spacing:1px}
.brand-sub{left:0;width:1200px;top:192px;text-align:center;font-size:14px;letter-spacing:5px}
.lang{left:980px;top:14px;font-size:12px;letter-spacing:1px;color:#444}
.lang:before{content:"";display:inline-block;border:5px solid transparent;border-top-color:#444;margin-right:10px;vertical-align:-2px}
.menu-btn{left:1087px;top:0;width:113px;height:46px;background:var(--ink);color:var(--white);font-size:13px;display:flex;align-items:center;justify-content:center;letter-spacing:1px}

/* hero */
.hero{top:246px;left:0;width:1200px;height:440px;background:linear-gradient(100deg,#6f767c 0%,#a9b1b7 35%,#c9ced2 55%,#9ca3a9 80%,#5f666c 100%)}
.hero-title{left:0;width:1200px;top:76px;text-align:center;color:var(--white)}
.hero-title .l1{font-size:37px;font-weight:700;line-height:46px}
.hero-title .l2{font-size:33px;font-weight:400;line-height:40px}
.hero-lede{left:0;width:1200px;top:222px;text-align:center;color:var(--white);font-size:21px;line-height:30px;font-weight:400}

/* team */
.section-title{left:0;width:1200px;text-align:center;font-size:33px;line-height:42px;font-weight:400;text-transform:uppercase}
.section-title b{font-weight:700}
.divider{left:297px;top:1056px;width:606px;height:1px;background:var(--rule)}
.method-title{left:0;width:1200px;top:1112px;text-align:center;font-size:31px;font-weight:700}

.card{position:absolute;width:495px;height:263px;color:var(--white);text-align:center}
.card h3{font-size:23px;font-weight:700;margin-top:95px;text-transform:uppercase}
.card p{font-size:14.5px;line-height:1.6;width:380px;margin:10px auto 0}

/* areas */
.areas{top:1793px;left:0;width:1200px;height:390px;background:var(--grey-band)}

/* split */
.split-rule{left:599px;top:2250px;width:1px;height:272px;background:var(--rule)}
.split-title{font-size:33px;font-weight:400;width:600px;text-align:center}

/* contact */
.contact{top:2592px;left:0;width:1200px;height:449px;background:linear-gradient(90deg,#c9dbe3 0%,#dfe8ec 50%,#eef2f4 100%)}
.contact-photo{left:820px;top:0;width:380px;height:449px;background:linear-gradient(90deg,rgba(230,236,240,0) 0%,#c2ccd3 40%,#8f9aa3 100%)}
.contact-title{left:136px;top:92px;font-size:37px;line-height:44px;text-transform:uppercase;color:#1a1a1a}
.contact-title b{font-weight:700}
.contact-copy{left:136px;top:184px;width:580px;font-size:14.5px;line-height:1.6;color:#222}
.contact-mail{left:136px;top:344px;font-size:30px;color:#1a1a1a}

/* footer */
.site-footer{top:3041px;left:0;width:1200px;height:347px;background:var(--footer);color:var(--footer-text)}
.fcol{position:absolute;top:52px;font-size:13.5px;line-height:22px}
.fcol h4{font-size:14px;font-weight:600;text-transform:uppercase;letter-spacing:.5px;margin-bottom:14px;color:#ddd}
.email-field{position:absolute;left:856px;top:170px;width:182px;height:35px;background:var(--white);color:#555;font-size:13px;padding:9px 10px}
.subscribe{position:absolute;left:856px;top:211px;width:182px;height:32px;background:var(--btn-grey);color:var(--white);font-size:13px;font-weight:700;display:flex;align-items:center;justify-content:center;letter-spacing:.5px}
.footer-mail{left:136px;top:228px;font-size:13.5px}
.copyright{left:136px;top:316px;font-size:12px}
</style>
</head>
<body>

<header class="abs site-header">
  <div class="abs brand-mark" aria-hidden="true"></div>
  <div class="abs brand-name">toravi</div>
  <div class="abs brand-sub">RECRUITMENT</div>
  <div class="abs lang">ENGLISH</div>
  <div class="abs menu-btn">MENU</div>
</header>

<section class="abs hero" role="img" aria-label="Misty grey mountain landscape with low clouds">
  <div class="abs hero-title">
    <div class="l1">LOREM IPSUM DOLOR SIT AMET, CONSECTETUR</div>
    <div class="l2">ADIPISCING ELITIVA MUUSCE CONSECTETUR</div>
    <div class="l2">TEMPUS URNA SED SUSCIPIT.</div>
  </div>
  <div class="abs hero-lede">Vitae odio eget augue. Donec pretium<br>fermentum tempor. Praesent rhoncus eget augue in rutrvulum accumsant.</div>
  <div class="btn-outline" style="left:99px;top:327px;width:215px;height:51px">Concept</div>
  <div class="btn-outline" style="left:359px;top:327px;width:226px;height:51px">Values</div>
  <div class="btn-outline" style="left:621px;top:327px;width:218px;height:51px">Social</div>
  <div class="btn-outline" style="left:878px;top:327px;width:215px;height:51px">Dubai 2020</div>
</section>

<section class="team">
  <h2 class="abs section-title" style="top:742px">Tempus urna sed suscipit.<br>Adipiscing <b>team</b> muusce consectetur.</h2>
  <p class="abs copy" style="left:0;width:1200px;top:842px">Lorem ipsum dolor sit amet, consectetur adipiscing elit. Vivamus ullamcorper enim non laoreet rutrum.<br>Fusce consectetur tempus urna sed suscipit.<br>Praesent vitae odio eget augue viverra varius nec ut turpis.</p>
  <div class="btn" style="left:93px;top:949px;width:181px;height:39px">Team Bio</div>
  <div class="btn" style="left:299px;top:949px;width:181px;height:39px">How We Help</div>
  <div class="btn" style="left:494px;top:949px;width:203px;height:39px">Free Consultation</div>
  <div class="btn" style="left:726px;top:949px;width:178px;height:39px">Free Advice</div>
  <div class="btn" style="left:932px;top:949px;width:172px;height:39px">Article</div>
  <div class="abs divider"></div>
</section>

<section class="methodology">
  <h2 class="abs method-title">METHODOLOGY</h2>
  <article class="card" style="left:93px;top:1178px;background:linear-gradient(120deg,#7d7a78,#4f4c4b 60%,#3a3a3c)" role="img" aria-label="Group of smiling team members, darkened">
    <h3>We Believe</h3>
    <p>Lorem ipsum dolor sit amet, cce consectetur tempus urna sed suscipit. Praesent vitae odio eget augue.</p>
  </article>
  <article class="card" style="left:604px;top:1178px;background:linear-gradient(120deg,#4b5a3a,#343c2c 55%,#2c2f2a)" role="img" aria-label="Orange flower in a green meadow, darkened">
    <h3>True Nature</h3>
    <p>Lorem ipsum dolor sit amet, cce consectetur tempus urna sed suscipit. Praesent vitae odio eget augue.</p>
  </article>
  <article class="card" style="left:93px;top:1454px;background:linear-gradient(120deg,#6d6d6d,#555 55%,#5a3f3c)" role="img" aria-label="Spool of red thread on a grey surface, darkened">
    <h3>Micro Thread</h3>
    <p>Lorem ipsum dolor sit amet, cce consectetur tempus urna sed suscipit. Praesent vitae odio eget augue.</p>
  </article>
  <article class="card" style="left:604px;top:1454px;background:linear-gradient(120deg,#4a4a4a,#5e5e5e 60%,#6e6e6e)" role="img" aria-label="Row of empty chairs against a grey wall, darkened">
    <h3>TORAVI™ Model</h3>
    <p>Lorem ipsum dolor sit amet, cce consectetur tempus urna sed suscipit. Praesent vitae odio eget augue.</p>
  </article>
</section>

<section class="abs areas">
  <h2 class="abs section-title" style="top:92px">Tempus urna sed suscipit.<br>Adipiscing <b>specialist areas</b> urna</h2>
  <p class="abs copy" style="left:0;width:1200px;top:178px">Lorem ipsum dolor sit amet, consectetur adipiscing elit. Vivamus ullamcorper enim non laoreet rutrum.<br>Fusce consectetur tempus urna sed suscipit.<br>Praesent vitae odio eget augue viverra varius nec ut turpis.</p>
  <div class="btn" style="left:404px;top:280px;width:178px;height:37px">All Areas</div>
  <div class="btn" style="left:613px;top:280px;width:181px;height:37px">Why Us?</div>
</section>

<section class="split">
  <h2 class="abs split-title" style="left:0;top:2268px">CLIENTS</h2>
  <p class="abs copy" style="left:0;width:600px;top:2330px">Lorem ipsum dolor sit amet, consectetur adipiscing elit.<br>Vivamus ullamcorper enim non laoreet rutrum.<br>Fusce consectetur tempus urna sed suscipit.<br>Praesent vitae odio eget augue viverra varius nec ut turpis.</p>
  <div class="btn" style="left:141px;top:2451px;width:187px;height:40px">Clients Form</div>
  <div class="btn" style="left:353px;top:2451px;width:184px;height:40px">Testimonials</div>
  <div class="abs split-rule"></div>
  <h2 class="abs split-title" style="left:600px;top:2268px">CANDIDATES</h2>
  <p class="abs copy" style="left:600px;width:600px;top:2330px">Lorem ipsum dolor sit amet, consectetur adipiscing elit.<br>Vivamus ullamcorper enim non laoreet rutrum.<br>Fusce consectetur tempus urna sed suscipit.<br>Praesent vitae odio eget augue viverra varius nec ut turpis.</p>
  <div class="btn" style="left:666px;top:2451px;width:181px;height:40px">Submit CV</div>
  <div class="btn" style="left:873px;top:2451px;width:186px;height:40px">Questionnaires</div>
</section>

<section class="abs contact">
  <div class="abs contact-photo" role="img" aria-label="Professional man standing in profile with arms folded, light office backdrop"></div>
  <h2 class="abs contact-title">Tempus urna sed suscipit.<br><b>TORAVI Group</b> urna</h2>
  <p class="abs contact-copy">Lorem ipsum dolor sit amet, consectetur adipiscing elit.<br>Vivamus Fusce consectetur tempus urna sed suscipit. Praesent<br>vitae odio eget augue viverra varius nec ut turpis. Lorem ipsum<br>dolor sit amet, consectetur adipiscing elit.<br>Vivamus Fusce consectetur tempus urna sed suscipit. Praesent<br>vitae odio eget augue viverra varius nec ut turpis.</p>
  <div class="abs contact-mail">info@toravigroup.com</div>
</section>

<footer class="abs site-footer">
  <div class="fcol" style="left:136px">
    <h4>Contacts</h4>
    Harbour Tech Park<br>Block 7 office 112<br>PO Box 418203<br>Phone: +971 4 3180246<br>Fax: +971 4 3180247
  </div>
  <div class="fcol" style="left:395px">
    <h4>Need Help?</h4>
    Help Center<br>FAQ<br>Terms of Use<br>About our Company<br>Careers
  </div>
  <div class="fcol" style="left:644px">
    <h4>Follow Us</h4>
    Linkwell<br>Chirpline<br>Friendsquare<br>Circleplus
  </div>
  <div class="fcol" style="left:856px;width:200px">
    <h4>Email Newsletters</h4>
    Subscribe to receive<br>inspiration, ideas, and news<br>in your inbox.
  </div>
  <div class="email-field">Email address</div>
  <div class="subscribe">SUBSCRIBE</div>
  <div class="abs footer-mail">info@toravi.com</div>
  <div class="abs copyright">Copyright 2014 TORAVI . All Rights Reserved.</div>
</footer>

</body>
</html>
```